gastroenterology web site design seo optimized UI/ Ux design

I am a physician (gastroenterologist) and I need an SEO optimized/ UI /UX design web site designed with contact form, tracking, mobile website, with facebook, twitter, linked in and other social media page designed and linked.

I want to be ale to update the website myself in the future

there will be a possible news feed link to it as well if I find one online. there maybe short video clips on it as well like video reviews. or myself introducing myself and my practice. ( I will make the short clips).

there should be a link where people can enter their email or cell phone number and have the directions texted or emailed to them.

there will be an area wehre pt can request appointments online. this will just send a text or email to my scheduler to call them and schedule an appointment.

most of the information content can be found online on national websites

I anticipate the website to be up to 10-15 pages

Blue should be incorporated in the website as most medical websites have that color

rolan vesterik
Vesterik MD
Gastroenterology
555-304-9172
belmarq@examplemail.test

Reason: there are some designers pending submission. the deadline has been extended for 5 days. submit your designs ASAP. payment is guaranteed.

Target Market(s)

patients, other doctors referring

Industry/Entity Type

Cell Phone

Number of Pages Required

5+ page

Colors
0255a3
33a6d7
ffc214

Requirements
Must have
• I want a running banner on top (maybe 3-4 banners) that transition to the left
• ui/ux design
• mobile website as well
• Spanish version of website
• contact form
• appointment request option
• email or text directions
• facebook/twitter/linked in and other social media pages and links
Should not have
• flash as it does not work on some phones or ipads

```html
<!DOCTYPE html>
<html lang="en">
<head>
<meta charset="utf-8">
<title>Meridian Digestive Care</title>
<link href="https://fonts.googleapis.com/css2?family=Open+Sans:wght@400;600;700&family=Orbitron:wght@500&display=swap" rel="stylesheet">
<style>
:root{
  --blue:#0255a3;--sky:#33a6d7;--yellow:#ffc214;--ink:#555;--muted:#888;
  --line:#dcdcdc;--dark:#0c1a22;--darker:#08131a;--pale:#f4f5f6;--foot-text:#c9d1d6;
}
*{box-sizing:border-box;margin:0;padding:0}
html,body{width:709px;height:1200px;overflow:hidden}
body{position:relative;font-family:"Open Sans",Arial,sans-serif;color:var(--ink);background:#fff}
.abs{position:absolute}
.topbar{left:0;top:0;width:709px;height:62px;background:var(--pale)}
.brand{left:28px;top:22px;display:flex;align-items:center;gap:7px;font-size:11px;font-weight:700;color:var(--blue);letter-spacing:.3px}
.brand i{width:16px;height:16px;border-radius:50%;background:#c8222a;display:block}
.lang{left:508px;top:26px;font-size:7px;color:var(--muted)}
.social{top:22px;display:flex;gap:5px;left:589px}
.social span{width:17px;height:17px;display:block}
.nav{left:0;top:62px;width:709px;height:26px;background:linear-gradient(#1a6cc0,var(--blue));display:flex;font-size:7.5px;font-weight:600;color:#fff}
.nav a{display:flex;align-items:center;justify-content:center;border-right:1px solid rgba(255,255,255,.2);height:100%}
.nav a.on{background:var(--yellow);color:var(--blue)}
.hero{left:0;top:88px;width:709px;height:319px;background:radial-gradient(ellipse at 30% 40%,#f3f6f9,#d9e3ec 55%,#c8d6e2)}
.hero-photo{left:400px;top:88px;width:309px;height:319px;background:linear-gradient(90deg,rgba(230,236,241,0) 0%,#f4f7fa 22%,#ffffff 40%,#e9eef3 52%,#1f57a6 60%,#2c67b8 68%,#f2f5f8 76%,#ffffff 86%,#dfe6ec 100%)}
.arrow{top:234px;width:22px;height:22px;border-radius:50%;background:rgba(255,255,255,.6)}
.form{left:77px;top:130px;width:164px;height:305px;background:#fff;box-shadow:0 2px 6px rgba(0,0,0,.12);padding:16px 11px}
.form:before{content:"";position:absolute;left:0;top:0;right:0;height:3px;background:linear-gradient(90deg,#e74c3c 0 25%,#2ecc71 25% 50%,var(--sky) 50% 75%,#9b7fd4 75%)}
.form h2{font-weight:400;font-size:10.5px;color:#444;margin-bottom:10px;white-space:nowrap}
.form label{display:block;font-size:6.5px;color:#444;margin:8px 0 5px}
.field{height:21px;border:1px solid #e2e2e2;border-radius:2px;font-size:6.5px;color:#aaa;padding:6px}
.dates{display:flex;gap:3px}.dates .field{flex:1;text-align:center;padding:6px 0}
.send{margin:21px 0 0 81px;width:60px;height:21px;background:var(--blue);color:#fff;font-size:7px;font-weight:700;display:flex;align-items:center;justify-content:center;border-radius:2px}
.dots{left:343px;top:418px;display:flex;gap:4px}.dots i{width:4px;height:4px;border-radius:50%;background:#ccc}.dots i:first-child{background:var(--blue)}
.welcome{left:35px;top:464px;width:362px}
.welcome h1{font-size:12.5px;font-weight:600;color:#666}
.welcome h3{font-size:7px;font-weight:400;color:#555;margin:3px 0 9px}
.welcome p{font-size:6.4px;line-height:9.8px;color:#888;text-align:justify}
.portrait{float:left;width:55px;height:55px;background:linear-gradient(#c9b9a8,#e9e0d8);margin:0 13px 2px 0}
.video{left:416px;top:466px;width:256px;height:140px;background:linear-gradient(120deg,#b9c3c9,#e3e7ea 60%,#9aa8b1);border:2px solid #e8e8e8}
.banner{left:35px;top:636px;width:639px;height:46px;background:var(--blue);display:flex;align-items:center;padding-left:84px;color:#fff;font-size:13px}
.banner b{margin-left:28px;background:var(--yellow);color:#333;font-size:7.5px;font-weight:400;width:88px;height:17px;display:flex;align-items:center;justify-content:center}
.topic{top:713px;width:197px}
.topic div{height:95px}
.topic p{text-align:center;font-size:9.5px;color:#333;margin-top:14px}
.faq-h{left:35px;top:853px;font-size:12.5px;color:#777;font-weight:400}
.more{left:653px;top:858px;font-size:7px;color:#888}
.faq{left:35px;top:878px;width:638px;height:75px;border:1px solid var(--line);display:flex;padding:20px 10px}
.q{flex:1;padding:0 8px 0 30px;position:relative;border-right:1px solid #eee;font-size:6px;color:#888;line-height:8.6px}
.q:last-child{border:0}
.q i{position:absolute;left:10px;top:0;width:12px;height:12px;border-radius:50%;background:#bbb;color:#fff;font-style:normal;font-size:6.5px;text-align:center;line-height:12px}
.q b{display:block;font-size:6.3px;font-weight:600;color:#666;margin-bottom:6px;line-height:9px}
.q.on i{background:var(--blue)}.q.on b{color:var(--blue)}
.footer{left:0;top:1001px;width:709px;height:163px;background:var(--dark)}
.col{top:1034px;color:var(--foot-text)}
.col h4{font-size:7.2px;color:#fff;letter-spacing:.6px;font-weight:700}
.md{font-family:Orbitron,sans-serif;font-size:14px;color:#fff;letter-spacing:1px;margin:1px 0 2px;white-space:nowrap}
.col p,.col li{font-size:6.4px;line-height:10px;list-style:none}
.col li{line-height:12px}
.vline{top:1033px;width:1px;height:110px;background:#1d2c35}
.finput{height:17px;background:#1e2c34;font-size:6px;color:#aab3b9;padding:5px 6px;margin-top:6px}
.fbtn{margin:15px 0 0 76px;width:49px;height:14px;background:var(--yellow);color:#333;font-size:6.5px;display:flex;align-items:center;justify-content:center}
.bottom{left:0;top:1164px;width:709px;height:36px;background:var(--darker);font-size:6.5px;color:#c0c7cc}
.bottom .ic{left:35px;top:15px;display:flex;gap:9px}.bottom .ic i{width:6px;height:6px;border-radius:50%;background:#e6e6e6}
</style>
</head>
<body>
<header class="abs topbar"></header>
<div class="abs brand"><i></i>MERIDIAN DIGESTIVE CARE</div>
<div class="abs lang">Language: <svg width="14" height="6"><rect width="9" height="6" fill="#1c3f8f"/><path d="M11 2l2 0-1 2z" fill="#999"/></svg></div>
<div class="abs social"><span style="background:#2d4d8f"></span><span style="background:#4fb4e6"></span><span style="background:#c9432e"></span><span style="background:#1170a8"></span></div>
<nav class="abs nav">
  <a class="on" style="margin-left:35px;width:65px">HOME</a><a style="width:127px">PHYSICIANS &amp; STAFF</a><a style="width:118px">PATIENT SERVICES</a><a style="width:113px">LIST OF DISEASES</a><a style="width:64px">FAQ</a><a style="width:69px">ERCP</a><a style="width:82px">CONTACT US</a>
</nav>
<section class="abs hero" role="img" aria-label="Blurred bright clinic interior"></section>
<div class="abs hero-photo" role="img" aria-label="Physician in a white coat with a blue tie, holding a blue clipboard"></div>
<div class="abs arrow" style="left:20px"><svg width="22" height="22"><path d="M13 6l-5 5 5 5" stroke="#fff" fill="none" stroke-width="1.5"/></svg></div>
<div class="abs arrow" style="left:668px"><svg width="22" height="22"><path d="M9 6l5 5-5 5" stroke="#fff" fill="none" stroke-width="1.5"/></svg></div>
<form class="abs form">
  <h2>Appointment request form</h2>
  <label>Name</label><div class="field">Jhone doe</div>
  <label>Email</label><div class="field">Collaboration offer</div>
  <label>Phone</label><div class="field">3923210939</div>
  <label>Contact For</label><div class="field">Lorem ipsumdolor</div>
  <label>Date</label><div class="dates"><div class="field">--Month--</div><div class="field">--Date--</div><div class="field">--Year--</div></div>
  <div class="send">SEND</div>
</form>
<div class="abs dots"><i></i><i></i><i></i></div>
<section class="abs welcome">
  <h1>WELCOME!</h1>
  <h3>Northbrook, Cedar Ridge, Pinehaven &amp; Lakemont's Premier Provider of Gastroenterology Care</h3>
  <div class="portrait" role="img" aria-label="Portrait of the physician"></div>
  <p>Meridian Digestive Care's associates are Northbrook, Cedar Ridge, Pinehaven, Larkfield &amp; surrounding Lakemont's premier providers of gastroenterology care. Your digestive health is important and when it comes to your healthcare, only the very best will do. Our three Board-Certified fellowship-trained Gastroenterologists are also Internal Medicine physicians with specialization in the areas of digestive diseases, liver disease, and cancer. At Meridian Digestive Care, we perform the latest in state-of-the-art procedures and</p>
  <p style="margin-top:5px">Together, the combined talents of Dr. Mara Lindqvist, Dr. Rolan Vesterik and Dr. Teo Haverfield offer high-quality diagnosis and treatment of the entire digestive system, providing patient-first compassionate care. We sincerely appreciate your decision to select us as your health care provider. This is a responsibility we take very seriously. We want your visits to our office to be pleasant.</p>
</section>
<div class="abs video" role="img" aria-label="Video still of a doctor consulting with a patient">
  <svg class="abs" style="left:110px;top:50px" width="38" height="38"><circle cx="19" cy="19" r="17" fill="rgba(0,0,0,.15)" stroke="#fff" stroke-width="1.5"/><path d="M15 12l11 7-11 7z" fill="#fff"/></svg>
</div>
<div class="abs banner">Text Yourself to the Highest Quality Treament Available<b>Contact Us</b></div>
<div class="abs topic" style="left:35px"><div role="img" aria-label="Woman holding her abdomen" style="background:linear-gradient(90deg,#f1f1f1,#d8d8d8 60%,#bfa596)"></div><p>Abdominal Concerns</p></div>
<div class="abs topic" style="left:256px"><div role="img" aria-label="Illustration of the colon inside a body" style="background:radial-gradient(circle at 50% 45%,#8ec3ef,#1f5fa8 55%,#0c2f66)"></div><p>Colon Issue</p></div>
<div class="abs topic" style="left:483px"><div role="img" aria-label="Person holding their stomach" style="background:linear-gradient(#fff 0 20%,#c8c8c8 20% 75%,#2f4e80 75%)"></div><p>Reflux Problems</p></div>
<h2 class="abs faq-h">FAQ'S</h2>
<div class="abs more">More</div>
<div class="abs faq">
  <div class="q on"><i>1</i><b>WHY AVOID RED LIQUIDS?</b>The color red can persist in the colon and potentially look like blood</div>
  <div class="q"><i>2</i><b>WHY AVOID RED LIQUIDS?</b>The color red can persist in the colon and potentially look like blood</div>
  <div class="q"><i>3</i><b>WHY AVOID RED LIQUIDS?</b>The color red can persist in the colon and potentially look like blood</div>
  <div class="q"><i>3</i><b>-I FEEL LIKE VOMITING, WHAT SHOULD I DO?</b>It is important that you take your entire prep if at all possible.</div>
</div>
<footer class="abs footer"></footer>
<div class="abs col" style="left:35px;width:135px">
  <h4>ABOUT ME</h4><div class="md">VESTERIK MD</div>
  <p>Dr. Rolan Vesterik received his training in Gastroenterology and Liver Disease from the State University of</p>
  <p style="margin:2px 0 6px 115px">&#8594;</p>
  <p>&#9990;&nbsp; Phone: (555) 304-9180</p><p>&#9993;&nbsp; office@examplemail.test</p><p>&#9113;&nbsp; Fax: (555) 304-9181</p>
</div>
<div class="abs vline" style="left:193px"></div>
<div class="abs col" style="left:232px"><h4>USEFUL LINKS</h4><ul style="margin-top:10px"><li>HOME</li><li>PHYSICIANS &amp; STAFF</li><li>PATIENT SERVICES</li><li>LIST OF DISEASES</li><li>FAQ</li><li>ERCP</li><li>CONTACT US</li></ul></div>
<div class="abs vline" style="left:322px"></div>
<div class="abs col" style="left:363px;width:140px">
  <h4 style="font-weight:400">GET IN TOUCH</h4>
  <p style="margin-top:8px">Hours: Monday thru Thursday 8:30am – 5:00pm Friday: 8:30am - 2:pm</p>
  <p style="margin-top:6px;padding-left:9px">Cedar Ridge Clinic, Meridian Digestive Care, 4410 Orchard Pkwy, Ste 100 Cedar Ridge, ST 00410</p>
  <p style="margin-top:8px;padding-left:9px">Pinehaven Clinic, Meridian Digestive Care, 2275 Willow Bend Rd, Ste 204, Pinehaven, ST 00420</p>
</div>
<div class="abs vline" style="left:514px"></div>
<div class="abs col" style="left:546px;width:125px">
  <h4>CONTACT</h4><p style="margin-top:5px;color:#e4e8eb">Conecus iure posae volor remped modis</p>
  <div class="finput" style="margin-top:8px">Name</div><div class="finput">Enter your email address</div>
  <div class="fbtn">CONTACT</div>
</div>
<div class="abs bottom"><div class="abs ic"><i></i><i></i><i></i><i></i></div><div class="abs" style="left:553px;top:14px">© 2015 meridiancare. All rights reserved.</div></div>
</body>
</html>
```